Lake of the Ozarks Anniversary Flag

Looking for a flag design that incorporates the outline of the Lake of the Ozarks on a white background with some additional wording/ design incorporated. Would like the lake outline in Navy Blue. On the top of the flag "LAKE OF THE OZARKS" in all caps (possibly also in Navy Blue with a bright red outline. In the background, large and centered in subdued gray "90th." Bottom left corner "1931" and bottom right corner "2021." Possibly also add a compass somewhere (possibly in the void to the middle left area. This is a flag being designed for boats that is to commemorate the 90th anniversary of Lake of the Ozarks this year. I have a couple more lake outlines I have screenshotted but this website won't seem to download them. I can send them separate if that assists.

```html
<!DOCTYPE html>
<html lang="en">
<head>
<meta charset="utf-8">
<title>Lake of the Ozarks 90th Anniversary Flag</title>
<link rel="stylesheet" href="https://fonts.googleapis.com/css2?family=Graduate&family=Archivo+Black&display=swap">
<style>
  :root {
    --navy: #2a3990;
    --red: #ee1c25;
    --white: #ffffff;
    --numeral-fill: #d2d3d5;
    --numeral-edge: #9c9d9f;
    --backdrop: #ffffff;
  }
  html, body {
    margin: 0;
    padding: 0;
    width: 1200px;
    height: 716px;
    overflow: hidden;
    background: var(--backdrop);
  }
  .flag {
    display: block;
    width: 1200px;
    height: 716px;
  }
  .band-navy { fill: var(--navy); }
  .band-red { fill: var(--red); }
  .varsity {
    font-family: "Graduate", "Georgia", serif;
    font-weight: 400;
  }
  .varsity-outer { fill: var(--red); stroke: var(--red); stroke-width: 9; stroke-linejoin: miter; }
  .varsity-inner { fill: var(--navy); stroke: var(--white); stroke-width: 4; stroke-linejoin: miter; paint-order: stroke; }
  .numeral {
    font-family: "Archivo Black", "Arial Black", sans-serif;
  }
  .numeral-shadow { fill: var(--numeral-edge); }
  .numeral-face { fill: var(--numeral-fill); stroke: var(--numeral-edge); stroke-width: 3; paint-order: stroke; }
  .lake-map { fill: url(#lakeTone); }
  .compass-ring { fill: none; stroke: var(--navy); stroke-width: 1.2; }
  .compass-point { fill: var(--navy); }
  .compass-point-light { fill: var(--white); stroke: var(--navy); stroke-width: 1; }
  .compass-letter {
    font-family: "Graduate", "Georgia", serif;
    font-size: 13px;
    fill: var(--navy);
    text-anchor: middle;
    dominant-baseline: middle;
  }
</style>
</head>
<body>
<svg class="flag" viewBox="0 0 1200 716" xmlns="http://www.w3.org/2000/svg" aria-label="Lake of the Ozarks 90th anniversary flag, 1931 to 2021">
  <defs>
    <radialGradient id="lakeTone" cx="50%" cy="50%" r="50%">
      <stop offset="0%" stop-color="#2a3990" stop-opacity="0.55"/>
      <stop offset="70%" stop-color="#2a3990" stop-opacity="0.25"/>
      <stop offset="100%" stop-color="#2a3990" stop-opacity="0"/>
    </radialGradient>
  </defs>

  <rect width="1200" height="716" fill="#ffffff"/>

  <!-- top border -->
  <rect class="band-navy" x="0" y="0" width="1200" height="10"/>
  <rect class="band-red" x="0" y="17" width="1200" height="6"/>

  <!-- title -->
  <g class="varsity">
    <text class="varsity-outer" x="51" y="118" font-size="92" textLength="1098" lengthAdjust="spacingAndGlyphs">LAKE OF THE OZARKS</text>
    <text class="varsity-inner" x="51" y="118" font-size="92" textLength="1098" lengthAdjust="spacingAndGlyphs">LAKE OF THE OZARKS</text>
  </g>

  <!-- anniversary numeral -->
  <g class="numeral">
    <text class="numeral-shadow" x="56" y="533" font-size="410" textLength="752" lengthAdjust="spacingAndGlyphs">90</text>
    <text class="numeral-face" x="48" y="525" font-size="410" textLength="752" lengthAdjust="spacingAndGlyphs">90</text>
    <text class="numeral-shadow" x="838" y="394" font-size="230" textLength="322" lengthAdjust="spacingAndGlyphs">th</text>
    <text class="numeral-face" x="830" y="386" font-size="230" textLength="322" lengthAdjust="spacingAndGlyphs">th</text>
  </g>

  <!-- lake outline area -->
  <ellipse class="lake-map" cx="556" cy="420" rx="400" ry="282" role="img" aria-label="Navy blue outline map of Lake of the Ozarks"/>

  <!-- compass -->
  <g class="compass" transform="translate(1037 482)">
    <circle class="compass-ring" r="34"/>
    <circle class="compass-ring" r="28"/>
    <polygon class="compass-point-light" points="0,0 -14,-14 -5,-5"/>
    <polygon class="compass-point" points="0,-46 6,-6 0,0 -6,-6"/>
    <polygon class="compass-point" points="46,0 6,6 0,0 6,-6"/>
    <polygon class="compass-point" points="0,46 -6,6 0,0 6,6"/>
    <polygon class="compass-point" points="-46,0 -6,-6 0,0 -6,6"/>
    <polygon class="compass-point" points="22,-22 4,-2 0,0 2,-4"/>
    <polygon class="compass-point" points="22,22 2,4 0,0 4,2"/>
    <polygon class="compass-point" points="-22,22 -4,2 0,0 -2,4"/>
    <polygon class="compass-point" points="-22,-22 -2,-4 0,0 -4,-2"/>
    <text class="compass-letter" x="0" y="-55">N</text>
    <text class="compass-letter" x="55" y="1">E</text>
    <text class="compass-letter" x="0" y="57">S</text>
    <text class="compass-letter" x="-56" y="1">W</text>
  </g>

  <!-- years -->
  <g class="varsity">
    <text class="varsity-outer" x="51" y="676" font-size="92" textLength="213" lengthAdjust="spacingAndGlyphs">1931</text>
    <text class="varsity-inner" x="51" y="676" font-size="92" textLength="213" lengthAdjust="spacingAndGlyphs">1931</text>
    <text class="varsity-outer" x="920" y="676" font-size="92" textLength="229" lengthAdjust="spacingAndGlyphs">2021</text>
    <text class="varsity-inner" x="920" y="676" font-size="92" textLength="229" lengthAdjust="spacingAndGlyphs">2021</text>
  </g>

  <!-- bottom border -->
  <rect class="band-red" x="0" y="691" width="1200" height="6"/>
  <rect class="band-navy" x="0" y="704" width="1200" height="12"/>
</svg>
</body>
</html>
```